Flower delivery business needs sales brochure

I have a courier business that specialises in same-day flower deliveries; I want to make a single page A4 sales brochure (folded to DL) to give to our potential customers.
The company website is petalcouriers.net, this will give an idea of who we are and what we do, as well as some graphics and colours that we use.
When opened, the inside A4 space of the brochure will be a pricelist, so the entire page will be an excel table with delivery locations and prices; we will add the prices ourselves later, so ideally the inside will be a background of some sort that won't obstruct text. Maybe light/transparent flowers and a background colour?
The front of the DL brochure should be mostly a title page, so business name, phone number, a graphic?
The first inside page should relate to our service, there's a lot of info on our website that you could use, so same day delivery, 10:30 and 2:30 pick-up times, established over 10 years ago, air-conditioned vans, delivery to 300+ suburbs.
The back page would be contact details and maybe a summary of the key points of the 'about us' section of the website.

Industry/Entity Type

Business

```html
<!DOCTYPE html>
<html lang="en">
<head>
<meta charset="utf-8">
<title>Petal Couriers – Pricing &amp; Surcharges</title>
<link rel="stylesheet" href="https://fonts.googleapis.com/css2?family=Oswald:wght@700&family=Roboto+Condensed:wght@400;700&family=Montserrat:wght@600&display=swap">
<style>
  :root {
    --maroon: #551108;
    --maroon-line: #6a1f14;
    --red: #d3222a;
    --ink: #1c1c1c;
    --rule: #8e8e96;
    --frame: #b9b9c2;
    --page-bg: #e9e9ea;
    --white: #ffffff;
  }
  * { box-sizing: border-box; margin: 0; padding: 0; }
  html, body { width: 1200px; height: 1200px; overflow: hidden; }
  body {
    background: var(--page-bg);
    display: flex;
    align-items: center;
    justify-content: center;
    font-family: "Roboto Condensed", "Arial Narrow", sans-serif;
  }
  .spread {
    width: 1161px;
    height: 818px;
    display: grid;
    grid-template-columns: repeat(3, 1fr);
    grid-template-rows: 92px 1fr 59px;
  }
  .masthead, .contact-bar {
    grid-column: 1 / -1;
    background: var(--maroon);
    display: grid;
    grid-template-columns: repeat(3, 1fr);
  }
  .masthead > *, .contact-bar > * { border-right: 1px solid var(--maroon-line); }
  .masthead > *:last-child, .contact-bar > *:last-child { border-right: 0; }
  .masthead-art { position: relative; }
  .florist-photo {
    position: absolute;
    top: 4px;
    width: 180px;
    height: 98px;
    border-radius: 40px 40px 20px 20px;
    background: radial-gradient(ellipse at 30% 70%, #f2a21a 0%, #e8c42a 30%, rgba(85,17,8,0) 70%),
                radial-gradient(ellipse at 75% 55%, #f3e2c4 0%, #e79c5a 35%, rgba(85,17,8,0) 70%),
                linear-gradient(180deg, #8a4a2a, #3e1a10);
  }
  .masthead-art.left .florist-photo { right: 8px; }
  .masthead-art.right .florist-photo { left: 6px; transform: scaleX(-1); }
  .masthead-title {
    display: flex;
    align-items: center;
    justify-content: center;
    font-family: "Oswald", "Impact", sans-serif;
    font-weight: 700;
    font-size: 33px;
    letter-spacing: 1px;
    color: var(--white);
  }
  .panel {
    position: relative;
    background: linear-gradient(160deg, #f6eef3 0%, #f0dde6 30%, #e6dceb 55%, #f3e3ea 80%, #f7eef2 100%);
    padding: 10px 31px 0 30px;
    border-right: 1px solid #ffffff;
  }
  .panel:last-of-type { border-right: 0; }
  .price-list {
    width: 328px;
    border-collapse: collapse;
    border: 1px solid var(--frame);
    background: rgba(255,255,255,0.35);
  }
  .price-list th {
    height: 45px;
    text-align: left;
    color: var(--red);
    font-weight: 700;
    font-size: 20px;
    padding: 0 8px;
    border-bottom: 1px solid var(--rule);
  }
  .price-list td {
    height: 26.3px;
    font-size: 17px;
    color: var(--ink);
    padding: 0 8px;
    border-bottom: 1px solid var(--rule);
    line-height: 1;
  }
  .price-list tr:last-child td { border-bottom: 0; }
  .price-list .price { width: 78px; }
  .contact-bar > div {
    display: flex;
    align-items: center;
    justify-content: center;
    color: var(--white);
    font-family: "Montserrat", "Century Gothic", sans-serif;
    font-weight: 600;
    font-size: 20px;
  }
  .contact-phone { gap: 10px; font-size: 27px !important; }
  .phone-icon { width: 38px; height: 38px; }
</style>
</head>
<body>
<main class="spread">
  <header class="masthead">
    <div class="masthead-art left"><div class="florist-photo" role="img" aria-label="Smiling florist holding bright sunflowers, gerberas and a bouquet"></div></div>
    <h1 class="masthead-title">PRICING &amp; SURCHARGES</h1>
    <div class="masthead-art right"><div class="florist-photo" role="img" aria-label="Smiling florist holding bright sunflowers, gerberas and a bouquet"></div></div>
  </header>

  <section class="panel" role="img" aria-label="Soft faded pink flower background">
    <table class="price-list">
      <thead><tr><th>Delivery Areas</th><th class="price">Price</th></tr></thead>
      <tbody>
        <tr><td>Acacia Ridge</td><td class="price">000</td></tr>
        <tr><td>Albany Creek</td><td class="price">000</td></tr>
        <tr><td>Albion</td><td class="price">000</td></tr>
        <tr><td>Alderley</td><td class="price">000</td></tr>
        <tr><td>Alexandra Hills</td><td class="price">000</td></tr>
        <tr><td>Algester</td><td class="price">000</td></tr>
        <tr><td>Altandi</td><td class="price">000</td></tr>
        <tr><td>Annerley</td><td class="price">000</td></tr>
        <tr><td>Anstead</td><td class="price">000</td></tr>
        <tr><td>Aquatic Paradise</td><td class="price">000</td></tr>
        <tr><td>Archerfield</td><td class="price">000</td></tr>
        <tr><td>Arana Hills</td><td class="price">000</td></tr>
        <tr><td>Ascot</td><td class="price">000</td></tr>
        <tr><td>Ashgrove</td><td class="price">000</td></tr>
        <tr><td>Ashgrove West</td><td class="price">000</td></tr>
        <tr><td>Aspley</td><td class="price">000</td></tr>
        <tr><td>Auchenflower</td><td class="price">000</td></tr>
        <tr><td>Bald Hills</td><td class="price">000</td></tr>
        <tr><td>Balmoral</td><td class="price">000</td></tr>
        <tr><td>Banoon</td><td class="price">000</td></tr>
        <tr><td>Banyo</td><td class="price">000</td></tr>
        <tr><td>Bardon</td><td class="price">000</td></tr>
        <tr><td>Bardon West</td><td class="price">000</td></tr>
      </tbody>
    </table>
  </section>

  <section class="panel" role="img" aria-label="Soft faded pink flower background">
    <table class="price-list">
      <thead><tr><th>Delivery Areas</th><th class="price">Price</th></tr></thead>
      <tbody>
        <tr><td>Acacia Ridge</td><td class="price">000</td></tr>
        <tr><td>Albany Creek</td><td class="price">000</td></tr>
        <tr><td>Albion</td><td class="price">000</td></tr>
        <tr><td>Alderley</td><td class="price">000</td></tr>
        <tr><td>Alexandra Hills</td><td class="price">000</td></tr>
        <tr><td>Algester</td><td class="price">000</td></tr>
        <tr><td>Altandi</td><td class="price">000</td></tr>
        <tr><td>Annerley</td><td class="price">000</td></tr>
        <tr><td>Anstead</td><td class="price">000</td></tr>
        <tr><td>Aquatic Paradise</td><td class="price">000</td></tr>
        <tr><td>Archerfield</td><td class="price">000</td></tr>
        <tr><td>Arana Hills</td><td class="price">000</td></tr>
        <tr><td>Ascot</td><td class="price">000</td></tr>
        <tr><td>Ashgrove</td><td class="price">000</td></tr>
        <tr><td>Ashgrove West</td><td class="price">000</td></tr>
        <tr><td>Aspley</td><td class="price">000</td></tr>
        <tr><td>Auchenflower</td><td class="price">000</td></tr>
        <tr><td>Bald Hills</td><td class="price">000</td></tr>
        <tr><td>Balmoral</td><td class="price">000</td></tr>
        <tr><td>Banoon</td><td class="price">000</td></tr>
        <tr><td>Banyo</td><td class="price">000</td></tr>
        <tr><td>Bardon</td><td class="price">000</td></tr>
        <tr><td>Bardon West</td><td class="price">000</td></tr>
      </tbody>
    </table>
  </section>

  <section class="panel" role="img" aria-label="Soft faded pink flower background">
    <table class="price-list">
      <thead><tr><th>Delivery Areas</th><th class="price">Price</th></tr></thead>
      <tbody>
        <tr><td>Acacia Ridge</td><td class="price">000</td></tr>
        <tr><td>Albany Creek</td><td class="price">000</td></tr>
        <tr><td>Albion</td><td class="price">000</td></tr>
        <tr><td>Alderley</td><td class="price">000</td></tr>
        <tr><td>Alexandra Hills</td><td class="price">000</td></tr>
        <tr><td>Algester</td><td class="price">000</td></tr>
        <tr><td>Altandi</td><td class="price">000</td></tr>
        <tr><td>Annerley</td><td class="price">000</td></tr>
        <tr><td>Anstead</td><td class="price">000</td></tr>
        <tr><td>Aquatic Paradise</td><td class="price">000</td></tr>
        <tr><td>Archerfield</td><td class="price">000</td></tr>
        <tr><td>Arana Hills</td><td class="price">000</td></tr>
        <tr><td>Ascot</td><td class="price">000</td></tr>
        <tr><td>Ashgrove</td><td class="price">000</td></tr>
        <tr><td>Ashgrove West</td><td class="price">000</td></tr>
        <tr><td>Aspley</td><td class="price">000</td></tr>
        <tr><td>Auchenflower</td><td class="price">000</td></tr>
        <tr><td>Bald Hills</td><td class="price">000</td></tr>
        <tr><td>Balmoral</td><td class="price">000</td></tr>
        <tr><td>Banoon</td><td class="price">000</td></tr>
        <tr><td>Banyo</td><td class="price">000</td></tr>
        <tr><td>Bardon</td><td class="price">000</td></tr>
        <tr><td>Bardon West</td><td class="price">000</td></tr>
      </tbody>
    </table>
  </section>

  <footer class="contact-bar">
    <div class="contact-phone">
      <svg class="phone-icon" viewBox="0 0 40 40" aria-hidden="true">
        <circle cx="20" cy="20" r="20" fill="#1a1a1a"/>
        <path d="M14 9c1.5-.8 2.6-.3 3.2.9l1.6 3.4c.5 1 .2 2-.7 2.6l-1.3.9c.6 2.8 2.3 5.6 4.6 7.4l1.3-.8c.9-.6 2-.4 2.6.5l2.1 3.1c.7 1.1.5 2.3-.8 3-2.6 1.6-5.6 1-8.4-2C14.3 25.5 12 20.6 11.6 16c-.3-3 .6-5.6 2.4-7z" fill="#ffffff"/>
      </svg>
      <span>0400 123 567</span>
    </div>
    <div class="contact-email">Email : info@petalcouriers.net</div>
    <div class="contact-web">www.petalcouriers.net</div>
  </footer>
</main>
</body>
</html>
```